I own a self service Laundromat. From time to time our machines break or take the customers money. I would like to design a post card that I can send the customer that had trouble with one of the machines along with the return of their money. Maybe on one side of the card say OOPS! with a picture of a clothes washer or clothes dryer. On the other side some text that says we are sorry for the trouble at your last visit. Please see attached return of money and we would love to have you back and satisfied. Thank you again for visiting The Suds Corner. I currently don't have a logo so be as creative as you like.

```html
<!DOCTYPE html>
<html lang="en">
<head>
<meta charset="utf-8">
<title>The Suds Corner – Apology Postcard</title>
<link rel="stylesheet" href="https://fonts.googleapis.com/css2?family=Arimo:wght@400;700&display=swap">
<style>
  :root {
    --bg: #ececec;
    --card: #ffffff;
    --teal: #1f8f7e;
    --teal-dark: #0f4f45;
    --ink: #222222;
    --muted: #555555;
    --line: #777777;
    --photo-light: #e9e6e2;
    --photo-mid: #c9c4bd;
    --photo-cool: #a9b4bd;
  }
  * { box-sizing: border-box; margin: 0; padding: 0; }
  html, body { width: 900px; height: 1200px; overflow: hidden; }
  body {
    background: var(--bg);
    font-family: "Arimo", Arial, sans-serif;
    color: var(--ink);
    position: relative;
  }
  .postcard {
    position: absolute;
    left: 50px;
    width: 800px;
    height: 530px;
    background: var(--card);
    box-shadow: 0 4px 14px rgba(0,0,0,0.18);
    overflow: hidden;
  }
  .postcard--front { top: 50px; }
  .postcard--back { top: 620px; }

  /* Front */
  .front-photo {
    position: absolute; inset: 0;
    background: linear-gradient(120deg, var(--photo-light) 0%, var(--photo-mid) 45%, var(--photo-light) 60%, var(--photo-cool) 100%);
  }
  .front-swoosh { position: absolute; inset: 0; width: 100%; height: 100%; }
  .call-us {
    position: absolute; top: 18px; right: 0;
    background: var(--card);
    padding: 8px 22px 8px 16px;
    border-left: 4px solid var(--teal-dark);
    font-size: 20px; line-height: 1.15;
  }
  .call-us__number { font-size: 27px; }
  .oops {
    position: absolute; left: 130px; top: 150px;
    font-size: 150px; font-weight: 700; letter-spacing: 2px;
    color: #ffffff;
    -webkit-text-stroke: 6px var(--teal-dark);
    paint-order: stroke fill;
  }
  .website {
    position: absolute; left: 40px; bottom: 42px;
    font-size: 17px; color: var(--ink);
  }

  /* Back */
  .washer-photo {
    position: absolute; left: 40px; top: 22px;
    width: 270px; height: 210px;
    background: linear-gradient(90deg, #f4f4f4 0%, #d8dadc 40%, #f2f2f2 55%, #b9bcbf 100%);
    border-radius: 4px;
  }
  .apology {
    position: absolute; left: 30px; top: 250px; width: 300px;
    text-align: center; font-size: 20px; line-height: 1.3; color: var(--ink);
  }
  .apology__sorry { font-size: 28px; }
  .divider {
    position: absolute; left: 390px; top: 70px;
    width: 2px; height: 420px; background: var(--line);
  }
  .stamp-box {
    position: absolute; right: 40px; top: 22px;
    width: 66px; height: 66px; border: 2px solid var(--line);
  }
  .address-lines {
    position: absolute; left: 440px; top: 250px; width: 290px;
    list-style: none;
  }
  .address-lines li { height: 40px; border-bottom: 2px solid var(--line); }
</style>
</head>
<body>
  <article class="postcard postcard--front">
    <div class="front-photo" role="img" aria-label="Photo of two frustrated men beside broken washing machines in a laundry room"></div>
    <svg class="front-swoosh" viewBox="0 0 800 530" preserveAspectRatio="none" aria-hidden="true">
      <path d="M0 330 C 200 360, 420 420, 800 250 L 800 290 C 470 470, 200 420, 0 380 Z" fill="var(--teal)"/>
      <path d="M0 380 C 200 420, 470 470, 800 290 L 800 530 L 0 530 Z" fill="#ffffff" opacity="0.92"/>
      <path d="M560 0 C 600 120, 560 220, 430 300 L 470 300 C 620 210, 640 110, 600 0 Z" fill="var(--teal-dark)"/>
      <path d="M600 0 C 640 110, 620 210, 470 300 L 520 300 C 680 200, 680 90, 640 0 Z" fill="#ffffff" opacity="0.85"/>
    </svg>
    <div class="call-us">Call Us:<br><span class="call-us__number">0123-456-789</span></div>
    <h1 class="oops">OOPS!</h1>
    <p class="website">www.dummytext.com</p>
  </article>

  <article class="postcard postcard--back">
    <div class="washer-photo" role="img" aria-label="Photo of a white washing machine and a silver washing machine"></div>
    <p class="apology">we are <span class="apology__sorry">SORRY</span> for the trouble at your last visit. Please see attached return of money and we would love to have you back and satisfied. Thank you again for visiting The Suds Corner.</p>
    <div class="divider"></div>
    <div class="stamp-box"></div>
    <ul class="address-lines"><li></li><li></li><li></li><li></li></ul>
  </article>
</body>
</html>
```